Coralith Partners's New Branding
Anything the customer sees, we want to update
Coralith Partners's New Branding -
Creative Brief
Professional
Dorian Pelk, MCP
Director of Technology
418 West Alder Road Morton, IL 61552
dorian.pelk@coralithpt.example
www.coralithpt.example
In addition to branding our business cards, we're also looking to brand: 1) folders - two pockets w/ a slotted area on the left pocket to insert a business card 2) brochures - 8.5"x11" tri-fold brochure 3) letterhead 4) envelopes 5) sales proposal cover letter - Our logo and name - Presented to: "Customer's name" - Presented by: "our sales person(s)" - Title of presentation - our web address 6) powerpoint 7) binders (including spline) 8) cd label - Company's name we're presenting cd to - our logo and name - title of content on cd
Quote: "Our business is sustaining yours" Please layout the quote so that if we put a QR code on the back of the card in the future, it won't look out of place.

```html
<!DOCTYPE html>
<html lang="en">
<head>
<meta charset="utf-8">
<title>Coralith Partners – Folder and CD Label</title>
<link rel="stylesheet" href="https://fonts.googleapis.com/css2?family=Libre+Baskerville&display=swap">
<style>
  :root {
    --bg: #ececea;
    --paper: #ffffff;
    --green: #1f5b35;
    --green-deep: #154527;
    --green-light: #2f7a49;
    --ink: #2b2b2b;
    --line: #d6d6d6;
  }
  html, body { margin: 0; padding: 0; overflow: hidden; }
  body { width: 1200px; height: 862px; background: var(--bg); }
  .stage { display: block; width: 1200px; height: 862px; }
  .brand-name { font-family: "Libre Baskerville", Georgia, serif; fill: var(--ink); }
  .label-text { font-family: "Libre Baskerville", Georgia, serif; fill: #ffffff; }
  .fine-text { font-family: "Libre Baskerville", Georgia, serif; }
</style>
</head>
<body>
<svg class="stage" viewBox="0 0 1200 862" xmlns="http://www.w3.org/2000/svg">
  <defs>
    <radialGradient id="greenPanel" cx="50%" cy="55%" r="70%">
      <stop offset="0" stop-color="var(--green-light)"/>
      <stop offset="1" stop-color="var(--green-deep)"/>
    </radialGradient>
    <radialGradient id="mapTone" cx="50%" cy="50%" r="60%">
      <stop offset="0" stop-color="#e6e6e6"/>
      <stop offset="1" stop-color="#ffffff" stop-opacity="0"/>
    </radialGradient>
  </defs>

  <!-- Folder outside / inner flap -->
  <g class="folder-top">
    <rect x="91" y="29" width="480" height="343" fill="var(--paper)"/>
    <rect class="world-map" x="320" y="40" width="250" height="150" fill="url(#mapTone)" role="img" aria-label="Faint world map backdrop"/>
    <g class="folder-logo">
      <circle cx="118" cy="56" r="9" fill="var(--green)"/>
      <text class="brand-name" x="132" y="60" font-size="11">Coralith Partners</text>
    </g>
    <g class="folder-contact fine-text" fill="var(--green)" font-size="5.5">
      <text x="262" y="52">418 West Alder Road Morton, IL 61552</text>
      <text x="262" y="60">www.coralithpt.example</text>
    </g>
    <path class="pocket-left" d="M91 245 H300 Q327 245 327 272 V372 H91 Z" fill="url(#greenPanel)"/>
    <path class="pocket-right" d="M571 245 H362 Q335 245 335 272 V372 H571 Z" fill="url(#greenPanel)"/>
    <g class="card-slot">
      <rect x="158" y="300" width="62" height="20" fill="var(--paper)"/>
      <circle cx="166" cy="310" r="4" fill="var(--green)"/>
      <text class="brand-name" x="173" y="312" font-size="5">Coralith Partners</text>
    </g>
  </g>

  <!-- Folder cover: back and front -->
  <g class="folder-cover">
    <rect class="back-panel" x="91" y="384" width="240" height="461" fill="url(#greenPanel)"/>
    <text class="fine-text" x="175" y="561" font-size="5" fill="#cfe2d4">www.coralithpt.example</text>
    <text class="fine-text" x="185" y="716" font-size="5" fill="#cfe2d4">Our business is sustaining yours</text>
    <rect class="front-panel" x="331" y="384" width="240" height="461" fill="var(--paper)"/>
    <g class="cover-logo">
      <circle cx="402" cy="557" r="12" fill="var(--green)"/>
      <text class="brand-name" x="420" y="562" font-size="14">Coralith Partners</text>
    </g>
    <path class="front-pocket" d="M360 732 H571 V845 H331 V761 Q331 732 360 732 Z" fill="url(#greenPanel)"/>
    <line x1="402" y1="820" x2="500" y2="820" stroke="#cfe2d4" stroke-width="1"/>
  </g>

  <!-- CD label -->
  <g class="cd-label">
    <clipPath id="discClip"><circle cx="852" cy="420" r="163"/></clipPath>
    <circle cx="852" cy="420" r="163" fill="var(--paper)"/>
    <path d="M680 392 Q852 352 1030 392 V600 H680 Z" fill="url(#greenPanel)" clip-path="url(#discClip)"/>
    <circle cx="852" cy="420" r="163" fill="none" stroke="var(--line)" stroke-width="3"/>
    <g class="cd-logo">
      <circle cx="812" cy="288" r="9" fill="var(--green)"/>
      <text class="brand-name" x="826" y="292" font-size="11">Coralith Partners</text>
    </g>
    <text class="fine-text" x="852" y="316" font-size="5" fill="var(--green)" text-anchor="middle">www.coralithpt.example</text>
    <circle cx="852" cy="380" r="44" fill="var(--paper)" stroke="var(--line)" stroke-width="1.5"/>
    <circle cx="852" cy="380" r="28" fill="none" stroke="var(--line)" stroke-width="1.5"/>
    <circle cx="852" cy="380" r="14" fill="var(--bg)" stroke="var(--line)" stroke-width="1.5"/>
    <text class="label-text" x="852" y="460" font-size="10" text-anchor="middle">Title of content</text>
    <text class="label-text" x="852" y="500" font-size="8" text-anchor="middle" fill-opacity="0.9">Presenting to: “Company’s name”</text>
  </g>
</svg>
</body>
</html>
```